Flyer Promoting Dental Benefit Program

I want to promote a dental benefit program to my patients that do not have dental insurance. This flyer would be posted in our waiting room and where people make payments. The goal would be to get those interested to request more information and enroll in the program. I have a card that will be issued that has a logo. Theflyer and card should feel congruent. I've uploaded a file with a copy of that card.
The plan costs $290/person. It includes 2 cleanings, exams, and x-rays. It also includes a 20% discount off of our standard fees. The plan or membership lasts for one year. It is only available to those without insurance. It is also important to let people know that this is not insurance (some kind of a disclaimer).
Updates
This plan is only available to patients at my office. The contact information is: Harborview Dental, 2718 West 4600 North Suite 209, Salt Lake City, Utah 84097. (801) 555-0187. info@harborviewdental.example. It is not necessary to include contact information as this flyer will be used as in-office promotion.
Target Market(s)
Those without dental insurance, but have resources to afford dental care.
Industry/Entity Type
Insurance
Look and feel
Each slider illustrates characteristics of the customer's brand and the style your logo design should communicate.

```html
<!DOCTYPE html>
<html lang="en">
<head>
<meta charset="utf-8">
<title>Dental Benefit Program – Harborview Dental</title>
<link rel="stylesheet" href="https://fonts.googleapis.com/css2?family=Arimo:wght@400;700&display=swap">
<style>
  :root {
    --ink: #1d232b;
    --sage: #93a99c;
    --sage-box: #8fa597;
    --green: #4fd63a;
    --green-dark: #3cc22c;
    --red: #e8141b;
    --white: #ffffff;
  }
  * { margin: 0; padding: 0; box-sizing: border-box; }
  html, body { width: 933px; height: 1200px; overflow: hidden; background: var(--white); }
  body { font-family: "Arimo", Arial, sans-serif; font-weight: 700; }
  .flyer { position: relative; width: 933px; height: 1200px; overflow: hidden; background: var(--white); }

  .brand-mark {
    position: absolute; left: 36px; top: 42px; width: 112px; height: 112px;
    border-radius: 50%;
    background: radial-gradient(circle at 40% 35%, #7ef25c, var(--green-dark) 70%);
  }
  .program-title { position: absolute; left: 186px; top: 22px; }
  .program-title .word {
    display: block; font-size: 114px; line-height: 1; color: var(--ink); letter-spacing: -1px;
  }
  .program-title .sub {
    display: block; margin-top: 4px; font-size: 59px; line-height: 1; color: var(--sage); letter-spacing: 0.5px;
  }

  .sponsor { position: absolute; right: 33px; top: 34px; text-align: right; color: var(--sage); }
  .sponsor .by { font-size: 24px; letter-spacing: 0.3px; }
  .sponsor .name { margin-top: 4px; font-size: 37px; line-height: 1.1; }

  .ask-badge {
    position: absolute; left: 705px; top: 192px; width: 166px; height: 166px; border-radius: 50%;
    background: radial-gradient(circle at 45% 35%, #6fee4d, var(--green-dark) 75%);
    color: var(--white); text-align: center; padding-top: 20px;
  }
  .ask-badge .please { font-size: 32px; line-height: 1; }
  .ask-badge .ask { font-size: 56px; line-height: 1; color: var(--red); }
  .ask-badge .more { font-size: 15px; line-height: 1.15; margin-top: 2px; }

  .question {
    position: absolute; left: 40px; top: 224px; font-size: 66px; line-height: 64px; color: var(--sage);
  }

  .offer { position: absolute; left: 50px; top: 384px; color: var(--green); font-size: 52px; line-height: 64px; }
  .offer .price { color: var(--red); }
  .offer ul { list-style: none; }
  .offer li::before { content: "• "; }

  .photo-main {
    position: absolute; left: 36px; top: 788px; width: 391px; height: 259px;
    background: linear-gradient(120deg, #e9ecef 0%, #d8b9a4 40%, #9ecbe0 75%, #c9d6de 100%);
  }
  .photo-smile {
    position: absolute; left: 332px; top: 999px; width: 186px; height: 98px;
    background: linear-gradient(90deg, #c99a86, #e8d8d2 50%, #c48f7d);
  }

  .eligibility {
    position: absolute; left: 449px; top: 788px; width: 440px; height: 189px;
    background: var(--sage-box); color: var(--white);
    font-weight: 400; font-size: 35px; line-height: 42px; text-align: center;
    display: flex; align-items: center; justify-content: center;
  }

  .cta {
    position: absolute; left: 560px; top: 996px; width: 300px; text-align: center;
    color: var(--red); font-size: 46px; line-height: 54px;
  }

  .disclaimer {
    position: absolute; left: 17px; top: 1120px; width: 820px; text-align: center;
    color: var(--sage); font-size: 22px; line-height: 28px;
  }
</style>
</head>
<body>
<main class="flyer">
  <div class="brand-mark" aria-hidden="true"></div>
  <h1 class="program-title">
    <span class="word">DENTAL</span>
    <span class="sub">benefit program</span>
  </h1>

  <div class="sponsor">
    <div class="by">Brought to you by</div>
    <div class="name">Harborview<br>Dental</div>
  </div>

  <div class="ask-badge">
    <div class="please">Please</div>
    <div class="ask">ASK</div>
    <div class="more">for more<br>information</div>
  </div>

  <h2 class="question">Do You NOT have<br>Dental Insurance?</h2>

  <section class="offer">
    <p>Join our dental benefit plan for</p>
    <p><span class="price">$290</span> and enjoy the following:</p>
    <ul>
      <li>1 years cover</li>
      <li>2 Teeth cleaning sessions</li>
      <li>Exams and X-rays</li>
      <li>20% discount on standard fees</li>
    </ul>
  </section>

  <div class="photo-main" role="img" aria-label="Photo of a smiling patient in the dental chair during a check-up"></div>
  <div class="photo-smile" role="img" aria-label="Close-up photo of a bright white smile"></div>

  <div class="eligibility">
    <p>Membership available<br>to all patients at this<br>office who do not<br>currently have insurance</p>
  </div>

  <p class="cta">Why not<br>Join TODAY</p>

  <p class="disclaimer">Please be aware this plan is only available to patients at this office<br>and is NOT a substitute for insurance.</p>
</main>
</body>
</html>
```